A start-up to help youth sports programs needs a designed 4-Page PDF.

We need a 4-page PDF that will be included with an email to coaches and parents to give them an overview of our Bright Squads program, and their steps to get started.

We have just finished the webpage for the initiative - www.bright-squads-example.org.

We will use our TLW logo (not the www.TLWHoopsexample.com logo), as this program is for every sport. We have not created a Bright Squads logo as of yet, but would like one. The TLW logo should be small and not prominent, but the title Bright Squads should be large on the first page.

We would like to use our TLW colors of orange, black, gray and blue.

The design should not have images, clipart or graphics showing lots of sports. We just need something clean and professional.

Here is the doc with all the content, including the introductory emails (no action is needed on the emails) - https://files.example-docs.net/document/d/7qRt-ZmLw_8hYvXcP2sKd_41NbeFgHu0jT5oA3lE/edit

Font styles to use
Sans Serif

```html
<!DOCTYPE html>
<html lang="en">
<head>
<meta charset="utf-8">
<title>Bright Squads – Program Overview</title>
<link href="https://fonts.googleapis.com/css2?family=Poppins:wght@400;500;600;700;800&family=Arimo:wght@400;700&display=swap" rel="stylesheet">
<style>
:root{
  --orange:#f26522;
  --teal:#14a3bc;
  --black:#111111;
  --ink:#1c1c1c;
  --slate:#3b3b3b;
  --grey:#555555;
  --stage:#e9e7e8;
  --paper:#ffffff;
}
*{box-sizing:border-box;margin:0;padding:0}
html,body{width:1200px;height:1200px;overflow:hidden;background:var(--stage)}
body{position:relative;font-family:"Arimo",Arial,sans-serif;color:var(--ink)}
.page{position:absolute;width:364px;height:516px;background:var(--paper);overflow:hidden;box-shadow:0 4px 14px rgba(0,0,0,.18)}
.p1{left:207px;top:65px}.p2{left:631px;top:65px}.p3{left:207px;top:620px}.p4{left:627px;top:620px}
.top-band{position:absolute;left:0;top:0;width:364px;height:11px;display:block}
.footer{position:absolute;left:0;bottom:0;width:364px;height:45px;display:block}
.footer-url{position:absolute;left:8px;bottom:19px;font-family:"Poppins",sans-serif;font-size:12px;color:#fff;font-weight:400;white-space:nowrap;line-height:1}
.body{position:absolute;left:7px;right:7px;font-size:7.1px;line-height:1.5}
.brand{position:absolute;top:36px;left:0;right:0;display:flex;justify-content:center;align-items:center;gap:4px}
.brand-dot{width:20px;height:20px;border-radius:50%;background:var(--orange)}
.brand-name{font-family:"Poppins",sans-serif;font-weight:700;font-size:26px;color:var(--orange);line-height:1}
.title{position:absolute;top:78px;left:0;right:0;text-align:center;font-family:"Poppins",sans-serif;font-weight:700;font-size:30px;color:var(--black);line-height:1.2}
.subtitle{position:absolute;top:124px;left:0;right:0;text-align:center;font-family:"Poppins",sans-serif;font-size:12.4px;color:var(--slate)}
.rule{position:absolute;top:146px;left:0;right:0;height:1px;background:var(--orange)}
.h-orange{color:var(--orange);font-family:"Poppins",sans-serif;font-weight:600;font-size:9px;margin:9px 0 5px}
.h-teal{color:var(--teal);font-family:"Poppins",sans-serif;font-weight:600;font-size:9px;margin:9px 0 5px}
.h-dark{color:var(--slate);font-family:"Poppins",sans-serif;font-weight:500;font-size:9px;margin:9px 0 5px}
.just{text-align:justify}
ul.dots{list-style:none;padding-left:9px}
ul.dots li{position:relative;padding-left:7px;margin-bottom:3.5px;text-align:justify}
ul.dots li::before{content:"";position:absolute;left:0;top:3px;width:3.4px;height:3.4px;border-radius:50%;background:var(--orange)}
ul.teal li::before{background:var(--teal)}
.equation{position:absolute;left:63px;top:355px;width:238px;height:47px}
.eq-frame{position:absolute;inset:0;display:block}
.eq-line{position:absolute;top:4px;left:0;right:0;text-align:center;font-family:"Poppins",sans-serif;font-weight:600;font-size:9.4px}
.eq-eq{position:absolute;top:20px;left:0;right:0;text-align:center;font-size:8px;font-weight:700}
.eq-pill{position:absolute;left:17px;width:204px;top:37px;height:20px;border-radius:4px;background:var(--slate);color:#fff;font-family:"Poppins",sans-serif;font-weight:700;font-size:12.6px;text-align:center;line-height:20px;letter-spacing:.2px}
.c-orange{color:var(--orange)}.c-teal{color:var(--teal)}
.page-title{position:absolute;left:0;right:0;text-align:center;font-family:"Poppins",sans-serif;font-weight:700;font-size:14.5px;color:var(--black)}
.ideas{margin:10px 11px 12px 12px;border:1px solid var(--ink);border-radius:5px;overflow:hidden}
.ideas-head{background:var(--orange);color:#fff;font-weight:700;font-size:6.9px;padding:3px 6px}
.ideas ol{padding:4px 0 4px 37px;font-size:6.9px;line-height:1.75}
.sub-head{text-align:center;font-family:"Poppins",sans-serif;font-weight:600;font-size:9.6px;margin:7px 0 8px}
.fund{position:absolute;left:0;right:0}
.fund-label{position:relative;height:11px}
.fund-label svg{position:absolute;left:8px;top:0;display:block}
.fund-label span{position:absolute;left:17px;top:0;line-height:11px;color:#fff;font-family:"Poppins",sans-serif;font-weight:600;font-size:7px}
.fund-cols{display:grid;grid-template-columns:183px 140px;padding-left:22px;margin-top:4px}
.fund-cols ul{list-style:none}
.fund-cols li{position:relative;padding-left:7px;font-size:7.1px;line-height:12.2px}
.fund-cols li::before{content:"";position:absolute;left:0;top:4.6px;width:3.4px;height:3.4px;border-radius:50%;background:var(--orange)}
.fund.parent li::before{background:var(--teal)}
.fund.player li::before{background:var(--black)}
.meet{position:absolute;top:357px;left:0;right:0;text-align:center;font-family:"Poppins",sans-serif;font-weight:600;font-size:8.4px}
.name-badge{position:absolute;top:371px;left:119px;width:130px;height:17px;display:block}
.name-text{position:absolute;top:368px;left:0;right:0;text-align:center;font-family:"Poppins",sans-serif;font-weight:700;font-size:15px;color:#fff;line-height:21px}
.bio-band{position:absolute;left:0;right:0;top:387px;bottom:0;background:#121212;border-top:2.5px solid var(--teal)}
.portrait{position:absolute;left:0;top:0;bottom:0;width:131px;background:linear-gradient(160deg,#5a5a5a 0%,#2a2a2a 55%,#161616 100%)}
.bio{position:absolute;left:139px;right:6px;top:5px;color:#fff;font-size:6.2px;line-height:1.62;text-align:justify}
.bio p{margin-bottom:4px}
</style>
</head>
<body>

<!-- Page 1: overview -->
<section class="page p1">
  <svg class="top-band" viewBox="0 0 364 11"><polygon points="0,0 68,0 79,11 0,11" fill="#111"/><polygon points="72,0 134,0 145,11 83,11" fill="#14a3bc"/><polygon points="138,0 364,0 364,11 149,11" fill="#f26522"/></svg>
  <div class="brand"><span class="brand-dot"></span><span class="brand-name">TLW</span></div>
  <h1 class="title">Bright Squads</h1>
  <p class="subtitle">Giving Athletes the Experience They Deserve</p>
  <div class="rule"></div>
  <div class="body" style="top:168px">
    <p>Bright Squads has been designed to raise standards, reduce frustrations, and give teams the ultimate edge.</p>
    <h2 class="h-orange">Our “Fundamentals” help...</h2>
    <ul class="dots">
      <li><b>Coaches</b> understand the Fundamentals of being a great coach.</li>
      <li><b>Parents</b> discover the Fundamentals of being a supportive sports parent.</li>
      <li><b>Players</b> learn the Fundamentals of being a great athlete, teammate, and leader.</li>
    </ul>
    <h2 class="h-teal">We know your time is limited...</h2>
    <p class="just">Which is why our simple-to-apply Fundamentals videos are only a few minutes long. And in nearly no time, everyone will have a common language to use and clear expectations to uphold.</p>
    <h2 class="h-dark">The real magic...</h2>
    <p class="just">Beyond the initial viewing of the videos, the real magic is the weekly reinforcement and top-of-mind awareness of the Fundamentals — in real time during the season.</p>
  </div>
  <div class="equation">
    <svg class="eq-frame" viewBox="0 0 238 47" preserveAspectRatio="none"><polyline points="0.5,47 0.5,0.5 237.5,0.5 237.5,47" fill="none" stroke="#333" stroke-width="0.8"/><line x1="0.5" y1="47" x2="13" y2="47" stroke="#333" stroke-width="0.8"/><line x1="237.5" y1="47" x2="225" y2="47" stroke="#333" stroke-width="0.8"/></svg>
    <div class="eq-line">Better <span class="c-orange">Coaches</span> + Better Players + Better <span class="c-teal">Parents</span></div>
    <div class="eq-eq">=</div>
    <div class="eq-pill">A Better Sports Experience</div>
  </div>
  <svg class="footer" viewBox="0 0 364 45"><polygon points="0,0 186,0 209,28 364,28 364,45 0,45" fill="#111"/><polygon points="178,16 364,16 364,19.5 182,19.5" fill="#f26522"/></svg>
  <span class="footer-url">Bright-Squads-example.org</span>
</section>

<!-- Page 2: parents -->
<section class="page p2">
  <svg class="top-band" viewBox="0 0 364 11"><polygon points="0,0 68,0 79,11 0,11" fill="#111"/><polygon points="72,0 134,0 145,11 83,11" fill="#14a3bc"/><polygon points="138,0 364,0 364,11 149,11" fill="#f26522"/></svg>
  <h2 class="page-title" style="top:30px">Next Steps for <span class="c-teal">Parents</span>...</h2>
  <div class="body" style="top:64px">
    <h3 class="h-teal" style="font-size:7.6px">Step 1 - Watch the Initial Parent Fundamentals Course</h3>
    <ul class="dots teal">
      <li>Complete the 45-minute course and sign the code of conduct within the next 10 days.</li>
      <li>You will also have access to the Coach and Player Fundamentals courses.</li>
    </ul>
    <h3 class="h-teal" style="font-size:7.6px;margin-top:16px">Step 2 - Watch the Weekly Videos</h3>
    <ul class="dots teal">
      <li>Each Sunday, you will be emailed a weekly Parent Fundamentals video that reinforces one of the 10 Parent Fundamentals. Total time - 3-5 minutes.</li>
      <li>You will also receive two Player Fundamental videos for the week to watch with your child. At practice, the coach will take a few minutes to discuss how the players can apply these Fundamentals in the season.</li>
    </ul>
  </div>
  <svg class="footer" viewBox="0 0 364 45"><polygon points="0,0 186,0 209,28 364,28 364,45 0,45" fill="#111"/><polygon points="178,16 364,16 364,19.5 182,19.5" fill="#f26522"/></svg>
  <span class="footer-url">Bright-Squads-example.org</span>
</section>

<!-- Page 3: coaches -->
<section class="page p3">
  <svg class="top-band" viewBox="0 0 364 11"><polygon points="0,0 68,0 79,11 0,11" fill="#111"/><polygon points="72,0 134,0 145,11 83,11" fill="#14a3bc"/><polygon points="138,0 364,0 364,11 149,11" fill="#f26522"/></svg>
  <h2 class="page-title" style="top:26px">Next Steps for <span class="c-orange">Coaches</span>...</h2>
  <div class="body" style="top:60px">
    <h3 class="h-orange" style="font-size:7.6px">Step 1 - Watch the Initial Coach Fundamentals Course</h3>
    <ul class="dots">
      <li>Complete the 45-minute course and sign the code of conduct within the next 10 days. You will also have access to the Parent and Player Fundamentals courses to watch any time.</li>
    </ul>
    <h3 class="h-orange" style="font-size:7.6px;margin-top:14px">Step 2 - Show Your Team the Player Fundamentals Course</h3>
    <ul class="dots">
      <li>Introduce the players to the 16 Player Fundamentals as early in the season as possible. Time required - 60 minutes (The course includes videos &amp; discussion questions.)</li>
    </ul>
    <div class="ideas">
      <div class="ideas-head">Ideas For Showing the Course: (depending on time and availability of a quiet space &amp; wifi):</div>
      <ol>
        <li>Have a special team retreat pizza night and go through the course</li>
        <li>Show 4 Fundamental videos before or after your next 4 practices. (15 min each)</li>
        <li>Show the course between games at an early season tournament/event</li>
      </ol>
    </div>
    <h3 class="h-orange" style="font-size:7.6px">Step 3 - Watch the Weekly Videos for You and Your Team</h3>
    <ul class="dots">
      <li>Each Sunday, you will be emailed a Coach Fundamental video to watch to deepen your understanding of the topic. Total time - 3-5 minutes</li>
      <li>You will also receive two Player Fundamental videos for the week to show your team. Be sure to take a few minutes to celebrate players who are living out the Fundamentals of the week and to discuss how the team can further apply them.</li>
    </ul>
    <h3 class="sub-head">Can’t Show the Videos at Practice?</h3>
    <p class="just">If you don’t have a suitable, quiet space to watch the video as a team, request that your parents play the videos for their son or daughter on the drive to practice, as the weekly videos will be emailed to parents and players as well.</p>
  </div>
  <svg class="footer" viewBox="0 0 364 45"><polygon points="0,0 186,0 209,28 364,28 364,45 0,45" fill="#111"/><polygon points="178,16 364,16 364,19.5 182,19.5" fill="#f26522"/></svg>
  <span class="footer-url">Bright-Squads-example.org</span>
</section>

<!-- Page 4: fundamentals and instructor -->
<section class="page p4">
  <svg class="top-band" viewBox="0 0 364 11"><polygon points="0,0 68,0 79,11 0,11" fill="#111"/><polygon points="72,0 134,0 145,11 83,11" fill="#14a3bc"/><polygon points="138,0 364,0 364,11 149,11" fill="#f26522"/></svg>

  <div class="fund coach" style="top:31px">
    <div class="fund-label"><svg width="356" height="11" viewBox="0 0 356 11"><polygon points="0,0 100,0 108,11 0,11" fill="#f26522"/><polygon points="103,0 107,0 115,11 111,11" fill="#111"/><line x1="113" y1="10.5" x2="356" y2="10.5" stroke="#111" stroke-width="0.7"/></svg><span>Coach Fundamentals</span></div>
    <div class="fund-cols">
      <ul><li>Be Professional</li><li>Create a Safe Space</li><li>Enroll Parents</li><li>Connect Before You Correct</li><li>Set High Standards</li><li>Hold Others Accountable</li></ul>
      <ul><li>Run Effective Practices</li><li>Focus on the Process</li><li>Foster Teamwork</li><li>Instill Confidence</li><li>Develop Winners</li><li>Respect Officials</li></ul>
    </div>
  </div>

  <div class="fund parent" style="top:134px">
    <div class="fund-label"><svg width="356" height="11" viewBox="0 0 356 11"><polygon points="0,0 100,0 108,11 0,11" fill="#14a3bc"/><polygon points="103,0 107,0 115,11 111,11" fill="#111"/><line x1="113" y1="10.5" x2="356" y2="10.5" stroke="#111" stroke-width="0.7"/></svg><span>Parent Fundamentals</span></div>
    <div class="fund-cols">
      <ul><li>Be a Safe Space</li><li>Let Go</li><li>Foster Resilience</li><li>Make a Contribution</li><li>Protect Their Identity</li></ul>
      <ul><li>Respect Officials</li><li>Strengthen Bonds</li><li>Honor Boundaries</li><li>Support the Coach</li><li>Drop Your Fears</li></ul>
    </div>
  </div>

  <div class="fund player" style="top:226px">
    <div class="fund-label"><svg width="356" height="11" viewBox="0 0 356 11"><polygon points="0,0 100,0 108,11 0,11" fill="#3b3b3b"/><polygon points="103,0 107,0 115,11 111,11" fill="#111"/><line x1="113" y1="10.5" x2="356" y2="10.5" stroke="#111" stroke-width="0.7"/></svg><span>Player Fundamentals</span></div>
    <div class="fund-cols">
      <ul><li>Be Coachable</li><li>Be Grateful</li><li>Be Precise</li><li>Be the Best You</li><li>Be Unruffleable</li><li>Beat You-Yesterday</li><li>Hustle as a Habit</li><li>Light Up Others</li></ul>
      <ul><li>Lock In</li><li>Protect Your Confidence</li><li>Take Care of Your Body</li><li>Take Ultra Ownership</li><li>Think Like a Captain</li><li>Welcome Adversity</li><li>Be a Team Player</li><li>Be Consistent</li></ul>
    </div>
  </div>

  <p class="meet">Meet Your Instructor</p>
  <svg class="name-badge" viewBox="0 0 130 17"><polygon points="10,0 120,0 130,17 0,17" fill="#f26522"/></svg>
  <div class="bio-band">
    <div class="portrait" role="img" aria-label="Portrait photo of the instructor, Dario Venn, smiling in a dark polo shirt"></div>
    <div class="bio">
      <p>Dario is the President of TLW, the leading education program in the world for teaching basketball players how to think the game, lead their team, and develop a winning mindset.</p>
      <p>TLW impacts over 20,000 players and coaches each summer through 200+ camps across North America. Over 175,000 athletes and 15,000 coaches have attended TLW over the past 32 years.</p>
      <p>As a coach, Dario has led teams at nearly every level of play, from youth sports to high school sports to college teams. Dario is a highly sought-after speaker who has inspired over 250,000 students and educators around the world, and reaches hundreds of thousands online each year.</p>
    </div>
  </div>
  <div class="name-text">Dario Venn</div>
</section>

</body>
</html>
```